Vantorix needs a newsletter to introduce our new test - Helix Balance Profile

I need a newsletter or email design to introduce a new test that my company has to offer called Helix Balance Profile. We are launching this genetic test to fitness centers, nutritionists, high end gyms, personal trainers and others. The genetic test looks at 5 genetic markers that are key to how each individual processes nutrients, carbohydrates etc and then provides a comprehensive report for the individual on specific diet plans, exercise regimens and their genetic results. The newsletter should be an exciting announcement of this new test and one that can easily be used via email or via attachments. I have attached some files which provide much more detail. The final design should communicate an opportunity for these potential customers to increase revenue, provide their members with an extraordinary personalized genetic test and to provide a value add to their current offerings.
Updates
Hi,
I forgot to upload a one page marketing piece that i had created as well as the logo for vantorix. Happy to provide just not sure how to upload them into the project
Target Market(s)
fitness centers, high end gyms, nutritionists, dieticians, personal trainers, health coaches
Colors
Designer to choose colors to be used in the design.
Look and feel
Each slider illustrates characteristics of the customer's brand and the style your logo design should communicate.

```html
<!DOCTYPE html>
<html lang="en">
<head>
<meta charset="utf-8">
<title>Vantorix – Helix Balance Profile</title>
<link href="https://fonts.googleapis.com/css2?family=Poppins:wght@300;400;500;600;700&display=swap" rel="stylesheet">
<style>
:root{
  --navy:#1b2f73;
  --ink:#111111;
  --teal:#13b3a6;
  --band-a:#1f8f95;
  --band-b:#1c5f86;
  --dark:#1e2428;
  --link:#2a8cff;
  --white:#ffffff;
}
*{margin:0;padding:0;box-sizing:border-box}
html,body{width:1200px;height:2680px;overflow:hidden;background:var(--white)}
body{position:relative;font-family:'Poppins',sans-serif;color:var(--ink)}
.abs{position:absolute}

.hero{left:0;top:0;width:1200px;height:531px;background:linear-gradient(120deg,#3a3b3d 0%,#6b5a52 35%,#4a4040 60%,#2c2d30 100%)}
.brand{left:72px;top:60px;display:flex;align-items:center;gap:14px;color:var(--white);font-size:34px;font-weight:600}
.brand-dot{width:40px;height:40px;border-radius:50%;background:var(--teal)}
.hero-title{left:0;top:222px;width:1200px;text-align:center;color:var(--white);font-weight:700;font-size:27px;line-height:42px;text-transform:uppercase;letter-spacing:-.3px;text-shadow:0 2px 6px rgba(0,0,0,.45)}

.section-title{left:0;width:1200px;text-align:center;font-size:30px;font-weight:400;text-transform:uppercase}
.section-title b{font-weight:700}
.rule{left:547px;width:106px;height:2px;background:var(--navy)}

.factor{top:686px;width:200px;text-align:center;font-size:17px;font-weight:500;line-height:27px}
.factor svg{display:block;margin:0 auto 14px;width:64px;height:64px}

.frame{left:92px;top:1000px;width:484px;height:412px;background:var(--teal)}
.photo-a{left:77px;top:985px;width:484px;height:412px;background:linear-gradient(160deg,#f1eeec 0%,#d9c7bd 55%,#3bb6e0 100%)}
.pie{left:77px;top:985px;width:484px;height:412px}

.genes-bg{left:840px;top:960px;width:360px;height:480px;background:linear-gradient(90deg,rgba(255,255,255,0),#dcdcdc 60%,#ececec)}
.gene{left:654px;width:520px}
.gene h3{font-size:30px;font-weight:700;color:var(--navy);line-height:38px}
.gene p{font-size:21px;font-weight:300;color:#222;margin-top:4px}

.band{left:0;top:1510px;width:1200px;height:304px;background:linear-gradient(90deg,var(--band-a),var(--band-b))}
.band-quote{left:0;top:1568px;width:1200px;text-align:center;color:var(--white);font-size:25px;font-weight:700;line-height:38px}
.band-body{left:0;top:1658px;width:1200px;text-align:center;color:var(--white);font-size:16.5px;line-height:38px;font-weight:400}

.photo-b{left:68px;top:1912px;width:510px;height:368px;background:radial-gradient(ellipse at 50% 50%,#e8e8e8 0%,rgba(255,255,255,0) 75%)}
.benefits-title{left:77px;top:1960px;font-size:30px;font-weight:700;line-height:38px;text-transform:uppercase}
.benefits{left:77px;top:2052px;width:520px;list-style:none;font-size:16.5px;line-height:38px;font-weight:400}
.benefits li{display:flex;gap:8px;align-items:flex-start;margin-bottom:8px}
.benefits svg{flex:none;margin-top:12px}
.teal-block{left:762px;top:1902px;width:362px;height:333px;background:linear-gradient(160deg,#2cc3b3,#1a8f9d)}
.photo-c{left:680px;top:1951px;width:361px;height:333px;background:linear-gradient(150deg,#1e3a48 0%,#3c7a8d 55%,#c9583f 100%)}

.footer{left:0;top:2374px;width:1200px;height:306px;background:linear-gradient(180deg,#2a3136,var(--dark))}
.footer-quote{left:0;top:2470px;width:1200px;text-align:center;color:var(--white);font-size:45px;font-weight:700}
.footer-visit{left:0;top:2542px;width:1200px;text-align:center;color:var(--white);font-size:23px;font-weight:600}
.footer-visit a{color:var(--link);text-decoration:underline}
.copyright{left:0;top:2642px;width:1200px;text-align:center;color:var(--white);font-size:13px;font-weight:500}
</style>
</head>
<body>

<header class="abs hero" role="img" aria-label="Photo of a woman and a man stretching on a gym floor"></header>
<div class="abs brand"><span class="brand-dot"></span>Vantorix</div>
<h1 class="abs hero-title">Let us help you offer members a diet &amp; exercise ratio<br>that fits their genetic makeup!</h1>

<h2 class="abs section-title" style="top:613px"><b>Many factors can</b> lead to obesity</h2>
<div class="abs rule" style="top:664px"></div>

<div class="abs factor" style="left:52px">
  <svg viewBox="0 0 64 64" fill="none" stroke="#1b2f73" stroke-width="2"><rect x="8" y="8" width="30" height="44"/><path d="M14 18h4M14 26h18M14 32h18M14 38h12"/><rect x="40" y="36" width="16" height="18"/><path d="M40 42h16M40 48h16"/></svg>
  Side Effects of RX<br>Medicine</div>
<div class="abs factor" style="left:272px">
  <svg viewBox="0 0 64 64" fill="none" stroke="#1b2f73" stroke-width="2"><circle cx="32" cy="10" r="6"/><path d="M22 20h20v20H22zM26 40v18M38 40v18M22 22l-12 12M42 22l12 12"/></svg>
  Hormonal<br>Imbalances</div>
<div class="abs factor" style="left:494px">
  <svg viewBox="0 0 64 64" fill="none" stroke="#1b2f73" stroke-width="2"><circle cx="32" cy="18" r="10"/><path d="M14 56c0-12 8-20 18-20s18 8 18 20"/><rect x="22" y="44" width="20" height="10"/></svg>
  Failure to Control<br>Cravings</div>
<div class="abs factor" style="left:710px">
  <svg viewBox="0 0 64 64" fill="none" stroke="#1b2f73" stroke-width="2"><path d="M12 40h40l-4 14H16z"/><path d="M20 40l6-16h12l6 16"/><circle cx="50" cy="12" r="3"/><circle cx="12" cy="14" r="2"/></svg>
  Unhealthy<br>Diet</div>
<div class="abs factor" style="left:935px">
  <svg viewBox="0 0 64 64" fill="none" stroke="#1b2f73" stroke-width="2"><path d="M18 8h28v10c0 8 6 14 6 24 0 8-6 14-20 14S12 50 12 42c0-10 6-16 6-24z"/><path d="M32 30v26"/></svg>
  Lack of Appropriate<br>Exercise</div>

<h2 class="abs section-title" style="top:890px"><b>Helix Balance Profile</b> panel includes</h2>
<div class="abs rule" style="top:940px"></div>

<div class="abs genes-bg" role="img" aria-label="Faded photo of a woman doing a push-up"></div>
<div class="abs frame"></div>
<div class="abs photo-a" role="img" aria-label="Photo of a woman measuring her waist with a tape"></div>
<svg class="abs pie" viewBox="0 0 484 412">
  <path d="M310 279 L310 196 A83 83 0 1 1 241 233 Z" fill="#13b3a6"/>
  <path d="M310 279 L241 233 A83 83 0 0 1 310 196 Z" fill="#3a3a3a" transform="translate(-4 -4)"/>
  <text x="276" y="236" font-family="Poppins,sans-serif" font-size="13" fill="#fff">14%</text>
  <text x="243" y="280" font-family="Poppins,sans-serif" font-size="13" fill="#fff">86%</text>
  <text x="130" y="205" font-family="Poppins,sans-serif" font-size="14" font-style="italic" fill="#444">Non-Genetic Risk</text>
  <text x="139" y="257" font-family="Poppins,sans-serif" font-size="14" font-style="italic" fill="#444">Genetic Risk</text>
</svg>

<div class="abs gene" style="top:972px"><h3>FTO</h3><p>Appetite regulation and craving frequency</p></div>
<div class="abs gene" style="top:1066px"><h3>MC4R</h3><p>Metabolism regulation</p></div>
<div class="abs gene" style="top:1161px"><h3>FABP2</h3><p>Dietary fat sources and fat utilization</p></div>
<div class="abs gene" style="top:1254px"><h3>ADRB2</h3><p>Carbohydrate digestion and physical activity</p></div>
<div class="abs gene" style="top:1348px"><h3>SH2B1</h3><p>Regulation of leptin and insulin</p></div>

<section class="abs band" role="img" aria-label="Teal-tinted gym photo background"></section>
<p class="abs band-quote">"Genetics Play a Big Role...up to 86% of Healthy<br>Weight Levels are tied to Genetics."</p>
<p class="abs band-body">The Helix Balance Profile tests five genetic markers shown through research to be linked to an increased BMI.<br>Offer it to your members as a premium add-on that sets your gym, clinic or practice apart.</p>

<div class="abs photo-b" role="img" aria-label="Faded photo of a woman stretching"></div>
<h2 class="abs benefits-title">Benefits of offering genetic<br>testing</h2>
<ul class="abs benefits">
  <li><svg width="14" height="14" viewBox="0 0 14 14"><circle cx="7" cy="7" r="7" fill="#1b2f73"/><path d="M4 7l2 2 4-4" stroke="#fff" stroke-width="1.6" fill="none"/></svg><span>New revenue stream and a value add for your gym, clinic<br>or coaching practice</span></li>
  <li><svg width="14" height="14" viewBox="0 0 14 14"><circle cx="7" cy="7" r="7" fill="#1b2f73"/><path d="M4 7l2 2 4-4" stroke="#fff" stroke-width="1.6" fill="none"/></svg><span>Personalized Diet &amp; Exercise Plans for every member</span></li>
  <li><svg width="14" height="14" viewBox="0 0 14 14"><circle cx="7" cy="7" r="7" fill="#1b2f73"/><path d="M4 7l2 2 4-4" stroke="#fff" stroke-width="1.6" fill="none"/></svg><span>Customized meal plans and full recipes</span></li>
</ul>
<div class="abs teal-block" role="img" aria-label="Teal-tinted photo of a toned waist"></div>
<div class="abs photo-c" role="img" aria-label="Photo of a woman running on a treadmill"></div>

<footer class="abs footer" role="img" aria-label="Dark photo of people training in a gym"></footer>
<p class="abs footer-quote">“A goal without a plan is just a wish”</p>
<p class="abs footer-visit">Visit us at <a href="#">www.vantorix.com</a> to become a partner</p>
<p class="abs copyright">Copyright © 2019. All Rights Reserved</p>

</body>
</html>
```